Need a Car Magnet designed

I need a car magnet designed.

The dimensions have to be 9" width by 2.6" height.

It needs to say BLORVIK TOUR and include the attached logo

```html
<!DOCTYPE html>
<html lang="en">
<head>
<meta charset="utf-8">
<title>BLORVIK TOUR – Car Magnet</title>
<link href="https://fonts.googleapis.com/css2?family=Roboto+Condensed:ital,wght@0,900;1,900&display=swap" rel="stylesheet">
<style>
  :root {
    --backdrop-light: #93a8d0;
    --backdrop-dark: #6f84ad;
    --magnet-white: #fdfcfd;
    --stripe-grey: #636466;
    --tour-red: #ee2e26;
    --brand-navy: #1f418c;
    --text-white: #ffffff;
  }
  html, body {
    margin: 0;
    padding: 0;
    width: 1200px;
    height: 1000px;
    overflow: hidden;
  }
  .canvas {
    position: relative;
    width: 1200px;
    height: 1000px;
    background: radial-gradient(ellipse at 45% 30%, var(--backdrop-light) 0%, var(--backdrop-dark) 100%);
  }
  .car-magnet {
    position: absolute;
    left: 72px;
    top: 311px;
    width: 1058px;
    height: 305px;
    display: block;
  }
  .magnet-base { fill: var(--magnet-white); }
  .divider-stripe { fill: var(--stripe-grey); }
  .title-panel { fill: var(--tour-red); }
  .title-word {
    fill: var(--text-white);
    font-family: "Roboto Condensed", "Arial Narrow", sans-serif;
    font-weight: 900;
    font-style: italic;
  }
  .direction-arrow { fill: var(--text-white); }
  .direction-arrow-tail {
    fill: none;
    stroke: var(--text-white);
    stroke-width: 30;
  }
  .brand-dot { fill: var(--brand-navy); }
  .brand-name {
    fill: var(--brand-navy);
    font-family: "Roboto Condensed", "Arial Narrow", sans-serif;
    font-weight: 900;
    font-style: normal;
  }
</style>
</head>
<body>
<main class="canvas">
  <svg class="car-magnet" viewBox="0 0 1058 305" xmlns="http://www.w3.org/2000/svg" aria-label="BLORVIK TOUR car magnet">
    <rect class="magnet-base" x="0" y="0" width="1058" height="305"/>

    <!-- brand mark area -->
    <g class="brand-mark">
      <circle class="brand-dot" cx="58" cy="152" r="24"/>
      <text class="brand-name" x="96" font-size="44">
        <tspan x="96" y="146">BLORVIK</tspan>
        <tspan x="96" y="192">TOUR</tspan>
      </text>
    </g>

    <!-- slanted grey stripes and red title panel -->
    <polygon class="divider-stripe" points="286,0 308,0 394,305 372,305"/>
    <polygon class="title-panel" points="308,0 964,0 1036,305 394,305"/>
    <polygon class="divider-stripe" points="964,0 986,0 1058,305 1036,305"/>

    <!-- title -->
    <text class="title-word" x="368" y="151" font-size="178" textLength="562" lengthAdjust="spacingAndGlyphs">BLORVIK</text>
    <text class="title-word" x="672" y="281" font-size="156" textLength="300" lengthAdjust="spacingAndGlyphs">TOUR</text>

    <!-- curved arrow -->
    <g class="direction-arrow-group">
      <path class="direction-arrow-tail" d="M480,167 C478,225 520,258 580,230"/>
      <polygon class="direction-arrow" points="550,181 648,207 594,295"/>
    </g>
  </svg>
</main>
</body>
</html>
```